Business Card Design Project

We are rebranding an existing automotive collision repair business. The business is called dentworks garage. I have attached logo but I'm not tied to that. I want to leave this wide open.

I want this card to say we are professional, competent, cutting edge. We are focused on customers and use a lot of the latest technology to make the customer experience different. We sign customers in on iPads. Paperwork I signed electronically and updates are sent via text, email, logging on a website or as they wish. I want this innovation and image to come through in our cards

Target Market(s)

60%. Women 40% men. Age 35-60

Industry/Entity Type

Automotive

Requirements
Must have
• The card must have name, title, phone,email, cell, web page

```html
<!DOCTYPE html>
<html lang="en">
<head>
<meta charset="utf-8">
<title>dentworks garage – business card</title>
<link rel="stylesheet" href="https://fonts.googleapis.com/css2?family=Questrial&display=swap">
<style>
  :root {
    --stage: #2b2b2b;
    --card-white: #f7f7f7;
    --card-dark: #0b0d0a;
    --brand-green: #8cb82a;
    --glow-green: #6fd12c;
    --deep-green: #1d5a2a;
    --ink: #3d3d3d;
    --ink-soft: #5a5a5a;
    --paper-text: #ffffff;
  }
  html, body {
    margin: 0;
    width: 1200px;
    height: 901px;
    overflow: hidden;
    background: var(--stage);
    font-family: "Questrial", "Century Gothic", sans-serif;
  }
  .canvas {
    position: relative;
    width: 1200px;
    height: 901px;
  }
  .card {
    position: absolute;
    top: 300px;
    width: 520px;
    height: 300px;
    border-radius: 22px;
    overflow: hidden;
    box-shadow: 0 10px 30px rgba(0,0,0,0.45);
  }
  /* back side */
  .card--back {
    left: 50px;
    background: var(--card-dark);
  }
  .card--back .light-burst {
    position: absolute;
    inset: 0;
    background:
      radial-gradient(circle at 32% 42%, #eaffc0 0, var(--glow-green) 10%, rgba(60,160,50,0.75) 28%, rgba(20,80,35,0.55) 50%, transparent 72%),
      linear-gradient(115deg, var(--deep-green) 0%, #0f2a14 45%, var(--card-dark) 70%);
  }
  .card--back .brand-name {
    position: absolute;
    right: 34px;
    top: 120px;
    margin: 0;
    font-size: 32px;
    font-weight: 400;
    color: var(--paper-text);
    letter-spacing: 0.5px;
  }
  /* front side */
  .card--front {
    left: 630px;
    background: var(--card-white);
  }
  .card--front .brand-name {
    position: absolute;
    left: 36px;
    top: 38px;
    margin: 0;
    font-size: 34px;
    font-weight: 400;
    color: var(--brand-green);
    letter-spacing: 0.5px;
  }
  .card--front .rule {
    position: absolute;
    left: 36px;
    right: 40px;
    top: 98px;
    height: 1.5px;
    background: var(--brand-green);
  }
  .person {
    position: absolute;
    left: 36px;
    top: 126px;
  }
  .person__name {
    margin: 0;
    font-size: 23px;
    color: var(--brand-green);
  }
  .person__title {
    margin: 4px 0 0;
    font-size: 16px;
    color: var(--ink-soft);
  }
  .contact {
    position: absolute;
    margin: 0;
    padding: 0;
    list-style: none;
    font-size: 16px;
    color: var(--ink);
    line-height: 28px;
    white-space: nowrap;
  }
  .contact--phones { left: 36px; top: 206px; }
  .contact--online { left: 250px; top: 150px; }
  .contact__label {
    display: inline-block;
    width: 16px;
    color: var(--brand-green);
  }
</style>
</head>
<body>
<main class="canvas">
  <section class="card card--back">
    <div class="light-burst" role="img" aria-label="Green light burst of streaking translucent panels"></div>
    <p class="brand-name">dentworks garage</p>
  </section>

  <section class="card card--front">
    <p class="brand-name">dentworks garage</p>
    <div class="rule"></div>
    <div class="person">
      <p class="person__name">Martin Caldwell</p>
      <p class="person__title">Managing Director</p>
    </div>
    <ul class="contact contact--phones">
      <li><span class="contact__label">p</span> 0412 306 771</li>
      <li><span class="contact__label">c</span> 0498 152 640</li>
    </ul>
    <ul class="contact contact--online">
      <li><span class="contact__label">e</span> info@dentworksgarage.com</li>
      <li><span class="contact__label">w</span> www.dentworksgarage.com</li>
    </ul>
  </section>
</main>
</body>
</html>
```